Podcast tile image

Create me a cover image for a new podcast - "Pebble Lantern"
The podcast will be in the following category: business, career, and society and culture.

Target Market(s)

Women

Font styles to use
Sans Serif

Colors

Designer to choose colors to be used in the design.

Requirements
Nice to have
• A heart and a brain image.

```html
<!DOCTYPE html>
<html lang="en">
<head>
<meta charset="utf-8">
<title>Pebble Lantern – Podcast Cover</title>
<link rel="stylesheet" href="https://fonts.googleapis.com/css2?family=Open+Sans:wght@300;700&display=swap">
<style>
  :root {
    --bg-slate: #3a3e47;
    --bg-slate-deep: #262a31;
    --glow-red: #d81e16;
    --glow-red-soft: rgba(200, 24, 18, 0.55);
    --ink-white: #ffffff;
    --text-shadow: rgba(0, 0, 0, 0.45);
  }
  html, body {
    margin: 0;
    padding: 0;
    width: 1200px;
    height: 1200px;
    overflow: hidden;
    background: var(--bg-slate-deep);
  }
  .cover {
    position: relative;
    width: 1200px;
    height: 1200px;
    overflow: hidden;
    font-family: "Open Sans", Arial, sans-serif;
    color: var(--ink-white);
  }
  .cover-photo {
    position: absolute;
    inset: 0;
    background:
      radial-gradient(ellipse 330px 360px at 360px 560px, var(--glow-red) 0%, var(--glow-red-soft) 55%, rgba(200, 24, 18, 0) 100%),
      radial-gradient(ellipse at 55% 45%, var(--bg-slate) 0%, var(--bg-slate) 50%, var(--bg-slate-deep) 100%);
  }
  .cover-text {
    position: absolute;
    margin: 0;
    line-height: 1;
    white-space: nowrap;
    text-shadow: 3px 3px 5px var(--text-shadow);
  }
  .show-title-top {
    top: 40px;
    left: 0;
    width: 1148px;
    text-align: center;
    font-weight: 700;
    font-size: 212px;
    letter-spacing: -2px;
  }
  .show-title-main {
    top: 531px;
    right: 36px;
    font-weight: 700;
    font-size: 96px;
    letter-spacing: -1px;
  }
  .host-label {
    top: 808px;
    left: 642px;
    font-weight: 300;
    font-size: 70px;
  }
  .host-name {
    font-weight: 700;
    font-size: 108px;
    letter-spacing: -1px;
  }
  .host-name--first { top: 925px; left: 512px; }
  .host-name--last { top: 1066px; left: 836px; }
</style>
</head>
<body>
  <main class="cover">
    <div class="cover-photo" role="img" aria-label="Photo of a red beaded heart on a metal spring stem against a dark slate background"></div>

    <h1 class="cover-text show-title-top">PEBBLE</h1>
    <p class="cover-text show-title-main">LANTERN</p>
    <p class="cover-text host-label">WITH</p>
    <p class="cover-text host-name host-name--first">AUTHOR’S</p>
    <p class="cover-text host-name host-name--last">NAME</p>
  </main>
</body>
</html>
```